Create 2 X Google Templates and graphics for web portal

I would like to get a google slides 'theme' template for my business based off the company logo, this should include some images for a professional looking template. In addition a google doc template for some business documents (think FAQs, Knowledge Articles) and some images / graphics for use in a website (customer portal). This should be based on a theme using our branding colours, font and logo.

See attached brief.

```html
<!DOCTYPE html>
<html lang="en">
<head>
<meta charset="utf-8">
<title>Velora – Brand Templates</title>
<link href="https://fonts.googleapis.com/css2?family=Montserrat:wght@300;400;500;600;700&family=Varela+Round&display=swap" rel="stylesheet">
<style>
:root{
  --page:#f3f1f2;
  --slate:#6f8b9b;
  --slate-dark:#4f6878;
  --slate-light:#a9bcc7;
  --mist:#e6ebee;
  --pale:#f3f6f8;
  --red:#e23b3b;
  --ink:#4a4f55;
  --muted:#7b8288;
  --lav:#c9c8e4;
  --band:#d9dcde;
  --white:#fff;
}
*{box-sizing:border-box;margin:0;padding:0}
html,body{width:845px;height:1200px;overflow:hidden;background:var(--page)}
body{position:relative;font-family:Montserrat,sans-serif;color:var(--ink)}
.slide{position:absolute;width:370px;height:262px;background:var(--white);overflow:hidden;box-shadow:0 1px 3px rgba(0,0,0,.08)}
.abs{position:absolute}
.photo{position:absolute}
.brand{font-family:Montserrat,sans-serif;font-weight:300;letter-spacing:1px;color:var(--slate);line-height:1}
.tiny{font-size:3.6px;line-height:1.35;color:var(--muted)}
.small{font-size:4.3px;line-height:1.4;color:var(--ink)}
.h-round{font-family:"Varela Round",sans-serif;color:var(--slate)}
.label{font-weight:600;color:var(--slate-dark);font-size:6px}
ul.bullets{list-style:none}
ul.bullets li{position:relative;padding-left:4px;margin-bottom:6px}
ul.bullets li::before{content:"";position:absolute;left:0;top:1.6px;width:1.5px;height:1.5px;background:var(--ink)}
ul.boxes{list-style:none}
ul.boxes li::before{content:"";display:inline-block;width:2.6px;height:2.6px;border:.4px solid var(--ink);margin-right:2px;vertical-align:middle}
.accent-strip{position:absolute;height:4px;top:12px;left:0;width:56px;background:linear-gradient(90deg,#b8bdc2 0 50%,var(--lav) 50%)}
.foot-strip{position:absolute;bottom:0;height:3px;left:0;right:0;background:linear-gradient(90deg,transparent 0 38%,var(--lav) 38% 55%,transparent 55% 62%,#c3c7ca 62% 88%,var(--slate) 88%)}

/* cover */
.cover{left:237px;top:58px}
.cover .brand{position:absolute;top:60px;width:100%;text-align:center;color:#fff;font-size:34px;letter-spacing:3px}
.cover .tag{position:absolute;top:98px;width:100%;text-align:center;color:#fff;font-size:7px;letter-spacing:3px;font-weight:400}
.cover .url{position:absolute;top:118px;left:157px;width:57px;height:8px;border-radius:4px;background:#eef1f3;font-size:3.8px;font-weight:600;text-align:center;line-height:8px;color:var(--ink)}
.sq{position:absolute;background:rgba(255,255,255,.25)}

/* index */
.index{left:38px;top:338px}
.index .title{position:absolute;left:15px;top:21px;font-size:14px;font-weight:400;color:var(--slate);letter-spacing:.5px;border-bottom:.6px solid var(--slate);padding-bottom:1px;width:60px}
.index .title b{color:var(--red);font-weight:400}
.toc{position:absolute;left:34px;top:55px;width:248px}
.toc-row{display:flex;align-items:flex-end;height:16px}
.toc-row .t{font-size:5px;font-weight:600;color:var(--slate);line-height:1.1}
.toc-row .t span{display:block;font-weight:400;color:var(--ink);font-size:4.6px}
.toc-row .dots{flex:1;border-bottom:.5px dotted #999;margin:0 2px 1.5px}
.toc-row .n{font-size:5px;color:var(--ink)}
.sublist{position:absolute;left:62px;top:151px;width:220px}

/* slide header shared */
.sh-title{position:absolute;left:15px;top:20px;font-family:"Varela Round",sans-serif;font-size:15px;color:var(--slate);font-weight:700}
.sh-sub{position:absolute;left:15px;top:37px;font-size:6.5px;color:var(--ink);letter-spacing:.3px}
.sh-bar{position:absolute;top:23px;right:13px;height:9px;background:var(--slate)}
.sh-bar .brand{position:absolute;right:2px;top:-2px;font-size:12px;color:var(--white);background:var(--white);color:var(--slate);padding:0 2px}

/* release notes */
.release{left:436px;top:338px}
.quote{position:absolute;left:33px;top:51px;width:220px;height:33px;background:var(--pale);border-left:1px solid var(--slate);padding:7px 12px}
.rn-panel{position:absolute;left:262px;top:47px;width:95px;height:215px;background:var(--slate)}
.card{position:absolute;top:174px;width:57px;height:70px;border:.6px solid var(--slate-light);border-radius:3px;background:#fff;padding:0 3px}
.card .label{font-size:5.4px;border-bottom:.5px solid var(--slate-light);padding:2px 0 1px;margin-bottom:3px}

/* whats coming */
.coming{left:38px;top:618px}
.coming .side{position:absolute;left:13px;top:0;width:100px;height:262px;background:var(--slate)}
.coming .side h2{position:absolute;left:9px;top:20px;font-size:15px;color:#fff;line-height:1.05;font-weight:700;letter-spacing:.5px}
.coming .side h2 span{font-weight:400}
.coming .h1{position:absolute;left:124px;top:36px;font-size:15px;color:var(--slate);letter-spacing:.5px;border-bottom:1px solid var(--slate);padding-bottom:1px}
.manage{position:absolute;left:124px;top:94px;width:170px;border-top:.5px solid var(--ink);border-bottom:.5px solid var(--ink);padding:2px 0;font-size:6.6px;color:var(--slate-dark);line-height:1.15}
.manage b{font-weight:600}

/* service request */
.service{left:436px;top:618px}
.sr-grey{position:absolute;left:121px;top:44px;width:249px;height:56px;background:#a2a7aa}
.icon-grid{position:absolute;left:121px;top:110px;width:76px;height:72px;display:grid;grid-template-columns:1fr 1fr}
.icon-grid div{display:flex;align-items:center;justify-content:center}
.sr-band{position:absolute;left:11px;top:203px;width:347px;height:41px;background:var(--slate);display:flex;padding:13px 3px 0;gap:10px}
.sr-band p{flex:1;color:#fff;font-size:3.7px;line-height:1.35}
.circle-ic{position:absolute;top:195px;width:16px;height:16px;border-radius:50%;background:#fff}

/* knowledge */
.knowledge{left:38px;top:898px}
.kn-head{position:absolute;left:0;top:0;width:370px;height:63px;background:linear-gradient(100deg,#5b6f7b,#7f95a2 60%,#6a7f8b)}
.kn-head h2{position:absolute;left:15px;top:16px;font-family:"Varela Round",sans-serif;color:#fff;font-size:15px}
.kn-head .sub{position:absolute;left:15px;top:33px;color:#fff;font-size:8px;font-weight:300;letter-spacing:.3px}
.kn-head .tiny{position:absolute;left:15px;top:48px;color:#fff;width:200px}
.kn-head .brand{position:absolute;right:15px;top:22px;color:#fff;font-size:15px}
.sol-box{position:absolute;left:234px;top:78px;width:122px;height:160px;background:var(--mist);border:.6px solid var(--slate-light);padding:10px 8px}
.heading-h{font-family:"Varela Round",sans-serif;color:var(--slate);font-size:9px;display:flex;align-items:center;gap:4px}

/* faq */
.faq{left:436px;top:898px}
.faq-head{position:absolute;left:0;top:0;width:370px;height:48px;background:linear-gradient(90deg,#e8e9ea,#c4c6c8 55%,#8d9296)}
.faq-head h2{position:absolute;left:15px;top:13px;font-family:Montserrat,sans-serif;font-weight:700;font-size:14px;color:#222;border-bottom:1px solid #222;line-height:1}
.faq-head .sub{position:absolute;left:63px;top:21px;font-size:6.4px;color:#222}
.faq-head .brand{position:absolute;right:13px;top:15px;font-size:15px;color:#fff}
.qa{position:absolute;left:15px;width:200px;border-bottom:.5px solid #ccc;padding-bottom:3px}
.qa .q{font-size:5.6px;font-weight:600;color:var(--ink)}
.qa .q b,.qa .a b{color:var(--red);margin-right:3px;font-weight:700}
.qa .a{font-size:3.7px;line-height:1.35;color:var(--slate-dark);display:flex}
.qa .a b{color:var(--slate);font-size:5.5px;font-weight:400}
.pill{position:absolute;left:262px;width:93px;height:17px;border-radius:9px;background:var(--slate);display:flex;align-items:center;padding-left:2px;gap:6px}
.pill.hot{background:var(--red)}
.pill .dot{width:13px;height:13px;border-radius:50%;background:#d8dcdf}
.pill p{color:#fff;font-size:3.2px;line-height:1.3;width:60px}
.faq-panel{position:absolute;left:9px;top:182px;width:352px;height:80px;border-radius:14px 14px 0 0;background:var(--slate)}
.person{position:absolute;top:190px;width:51px;height:55px;border-radius:0 0 5px 5px;background:#fff;opacity:.88;padding:12px 3px 0;text-align:center}
.person .av{position:absolute;left:18px;top:-7px;width:15px;height:15px;border-radius:50%;background:#c9ced2;border:1px solid var(--slate-dark)}
.person .tiny{font-size:3.1px}
.person .who{font-size:3.2px;color:var(--muted);margin-top:5px}
</style>
</head>
<body>

<!-- Cover -->
<section class="slide cover">
  <div class="photo" role="img" aria-label="Climber resting on a rocky mountain summit above a misty valley" style="inset:0;background:linear-gradient(180deg,#8fa6b4 0%,#9fb2bd 40%,#7b8a93 62%,#4f5a61 85%,#8b8f92 100%)"></div>
  <div class="sq" style="left:40px;top:30px;width:34px;height:16px"></div>
  <div class="sq" style="left:20px;top:80px;width:18px;height:40px;background:rgba(255,255,255,.18)"></div>
  <div class="sq" style="left:68px;top:28px;width:16px;height:12px;background:rgba(190,140,140,.5)"></div>
  <div class="sq" style="left:26px;top:60px;width:16px;height:12px;background:rgba(190,140,140,.5)"></div>
  <div class="sq" style="left:345px;top:22px;width:14px;height:60px"></div>
  <div class="sq" style="left:330px;top:86px;width:22px;height:22px;background:rgba(255,255,255,.15)"></div>
  <div class="brand">velora</div>
  <div class="tag">WE DELIVER SOLUTIONS</div>
  <div class="url">www.velora.com.au</div>
</section>

<!-- Index -->
<section class="slide index">
  <div class="photo" role="img" aria-label="Hiker standing on a cliff edge beside a tall rock face" style="left:244px;top:0;width:126px;height:262px;background:linear-gradient(90deg,#7f98a7,#6f7f86 55%,#7a5f52)"></div>
  <div class="abs" style="left:15px;top:0;width:3px;height:14px;background:var(--slate)"></div>
  <div class="abs" style="left:19px;top:0;width:3px;height:14px;background:#b9bec2"></div>
  <div class="abs" style="left:23px;top:0;width:3px;height:14px;background:var(--red)"></div>
  <div class="title"><b>IN</b>DEX</div>
  <div class="toc">
    <div class="toc-row"><div class="t">Whats Coming<span>in 2022 release</span></div><div class="dots"></div><div class="n">03</div></div>
    <div class="toc-row"><div class="t">Knowledge Articles<span>Find helpful information</span></div><div class="dots"></div><div class="n">04</div></div>
    <div class="toc-row"><div class="t">Release Notes<span>Read important information to releases of Skyline9</span></div><div class="dots"></div><div class="n">05</div></div>
    <div class="toc-row"><div class="t">Service Request<span>Log a case with us</span></div><div class="dots"></div><div class="n">06</div></div>
    <div class="toc-row"><div class="t">FAQ's<span>Answers to common questions</span></div><div class="dots"></div><div class="n">07</div></div>
    <div class="toc-row" style="margin-top:8px"><div class="t" style="font-size:3.6px;font-weight:400;color:var(--ink)">a) Dolor sit amet, consectetuer adipiscing elit,</div><div class="dots"></div><div class="n">07</div></div>
  </div>
  <div class="sublist tiny" style="top:164px;color:var(--ink)">
    b) Sed diam nonummy nibh euismod tincidunt ut laoreet<br>
    c) Bolore magna aliquam erat volutpat.<br>
    d) Ut wisi enim ad minim veniam, quis nostrud exerci<br>
    e) Tation ullamcorper suscipit lobortis
  </div>
  <div class="brand abs" style="left:4px;top:228px;transform:rotate(-90deg);transform-origin:left top;font-size:16px;color:var(--slate-light)">velora</div>
  <div class="abs" style="left:0;bottom:0;width:370px;height:3px;background:var(--slate)"></div>
</section>

<!-- Release notes -->
<section class="slide release">
  <div class="accent-strip"></div>
  <div class="sh-title">Release Notes</div>
  <div class="sh-sub">Read important information to releases of Skyline9</div>
  <div class="sh-bar" style="left:135px"><span class="brand">velora</span></div>
  <div class="quote tiny" style="color:var(--ink)">Dolor sit amet, consectetuer adipiscing elit, sed diam nonummy nibh euismod tincidunt ut laoreet dolore magna aliquam erat volutpat. Ut wisi enim ad minim veniam, quis nostrud <span style="color:#4a6fb0">@Sam Ortell @ Ida Venn</span></div>
  <div class="abs label" style="left:33px;top:89px;font-size:6.5px;color:var(--slate)">Background</div>
  <div class="abs tiny" style="left:33px;top:99px;width:190px;color:var(--ink)">Dolor sit amet, consectetuer adipiscing elit, sed diam nonummy nibh euismod tincidunt ut laoreet dolore magna aliquam erat volutpat. Ut wisi enim ad minim veniam, quis nostrud <span style="color:#4a6fb0">@Sam Ortell @ Ida Venn</span></div>
  <div class="abs" style="left:33px;top:118px;font-size:6px;font-weight:600;color:var(--ink)">To Do</div>
  <ul class="abs boxes small" style="left:33px;top:126px;font-size:4.4px;line-height:1.55">
    <li>Dolor sit amet, consectetuer adipiscing elit,</li>
    <li>Sed diam nonummy nibh euismod tincidunt ut laoreet</li>
    <li>Bolore magna aliquam erat volutpat.</li>
    <li>Ut wisi enim ad minim veniam, quis nostrud exerci</li>
    <li>Tation ullamcorper suscipit lobortis</li>
  </ul>
  <div class="abs" style="left:0;top:188px;width:262px;height:40px;background:var(--band)"></div>
  <div class="card" style="left:27px"><div class="label">Goals</div><p class="tiny">Dolor sit amet, consectetuer adipiscing elit, sed diam nonummy nibh euismod tincidunt ut laoreet dolore magna aliquam erat volutpat.<br><br>Ut wisi enim ad minim veniam, quis nostrud @Sam Ortell @ Ida Venn</p></div>
  <div class="card" style="left:93px"><div class="label">Metric</div><p class="tiny">Lorem ipsum dolor sit amet, consectetuer adipiscing elit, sed diam nonummy nibh euismod tincidunt ut laoreet dolore magna aliquam erat volutpat.</p></div>
  <div class="card" style="left:158px"><div class="label">How it tracks?</div><p class="tiny">1. Dolor sit amet, conse tetuer adipiscing elit,<br><br>2. Sed diam nonummy nibh euismod tincidunt laoreet<br><br>3. Bolore magna aliquam erat volutpat.<br><br>4. Ut wisi enim ad minim veniam, quis nostrud exerci</p></div>
  <div class="rn-panel"></div>
  <div class="photo" role="img" aria-label="Hand writing with a pen on paper" style="left:273px;top:61px;width:73px;height:140px;background:linear-gradient(160deg,#4f6a7c,#8ea6b3 55%,#dfe7ea)"></div>
  <div class="foot-strip"></div>
</section>

<!-- Whats coming -->
<section class="slide coming">
  <div class="side">
    <h2>WHATS<br><span>COMING</span></h2>
    <div class="photo" role="img" aria-label="Hands working on a laptop showing a business presentation" style="left:8px;top:63px;width:84px;height:167px;background:linear-gradient(180deg,#dde3e7,#8a9aa5 35%,#3f4d58 60%,#b39a88 85%,#6d7880)"></div>
  </div>
  <div class="abs" style="left:150px;top:0;width:120px;height:3px;background:linear-gradient(90deg,var(--slate) 0 35%,#c3c7ca 35% 70%,var(--lav) 70%)"></div>
  <div class="brand abs" style="right:15px;top:15px;font-size:14px">velora</div>
  <div class="h1">IN 2022 RELEASE</div>
  <p class="abs tiny" style="left:124px;top:63px;width:220px;color:var(--ink);font-size:4px">The Wattle 22 release for Skyline9 Payroll delivers a number of exciting enhancements designed to provide improved capability and efficiency in your workplace. Below are just some of the enhancements and updates that will have you looking forward to the release on the 26 Jan 2022</p>
  <div class="manage"><b>Manage your work schedules using</b><br><i>Work Schedule Manager</i></div>
  <ul class="abs bullets tiny" style="left:124px;top:127px;width:200px;color:var(--ink);font-size:3.9px">
    <li>Lorem ipsum dolor sit amet, consectetuer adipiscing elit, sed diam nonummy nibh euismod tincidunt ut laoreet dolore magna aliquam erat volutpat. Ut wisi enim ad minim veniam, quis nostrud exerci tation ullamcorper suscipit lobortis nisl ut aliquip ex ea</li>
    <li>Dolor sit amet, consectetuer adipiscing elit, sed diam nonummy nibh euismod tincidunt ut laoreet dolore magna aliquam erat volutpat. Ut wisi enim ad minim veniam, quis nostrud exerci tation ullamcorper suscipit lobortis nisl ut aliquip ex ea</li>
    <li>Consectetuer adipiscing elit, sed diam nonummy nibh euismod tincidunt ut laoreet dolore magna aliquam erat volutpat. Ut wisi enim ad minim veniam, quis nostrud exerci tation</li>
    <li>Lorem ipsum dolor sit amet, consectetuer adipiscing elit, sed diam nonummy nibh euismod tincidunt ut laoreet dolore magna aliquam erat volutpat. Ut wisi enim ad minim veniam, quis nostrud exerci tation ullamcorper suscipit lobortis nisl ut aliquip ex ea</li>
  </ul>
  <div class="foot-strip"></div>
</section>

<!-- Service request -->
<section class="slide service">
  <div class="accent-strip"></div>
  <div class="sh-title">Service Request</div>
  <div class="sh-sub">Log a Case with us</div>
  <div class="sh-bar" style="left:154px"><span class="brand">velora</span></div>
  <div class="sr-grey"></div>
  <div class="photo" role="img" aria-label="Business handshake over a smartphone" style="left:126px;top:49px;width:67px;height:47px;background:linear-gradient(135deg,#dfe8ef,#7f9bb3 50%,#3d5a75)"></div>
  <div class="abs" style="left:195px;top:49px;font-size:5.4px;font-weight:600;color:#fff">To Do</div>
  <ul class="abs boxes" style="left:195px;top:56px;color:#fff;font-size:4px;line-height:1.6">
    <li>Dolor sit amet, consectetuer adipiscing elit,</li>
    <li>Sed diam nonummy nibh euismod tincidunt ut laoreet</li>
    <li>Bolore magna aliquam erat volutpat.</li>
    <li>Ut wisi enim ad minim veniam, quis nostrud exerci</li>
    <li>Tation ullamcorper suscipit lobortis</li>
  </ul>
  <div class="abs label" style="left:30px;top:72px;color:var(--slate)">Client Background</div>
  <div class="abs" style="left:11px;top:86px;width:120px;height:103px;background:var(--band)"></div>
  <div class="photo" role="img" aria-label="Collage of business people at work" style="left:19px;top:95px;width:94px;height:85px;background:linear-gradient(135deg,#e7ebee,#9fb0bc 45%,#d5dbe0 70%,#6f8393)"></div>
  <div class="icon-grid">
    <div style="background:var(--slate)"><svg width="18" height="18" viewBox="0 0 24 24" fill="none" stroke="#fff" stroke-width="1.8" stroke-linecap="round"><path d="M5 3h4l2 5-3 2a12 12 0 0 0 6 6l2-3 5 2v4a2 2 0 0 1-2 2A17 17 0 0 1 3 5a2 2 0 0 1 2-2z"/></svg></div>
    <div style="background:#a2a7aa"><svg width="20" height="20" viewBox="0 0 24 24" fill="none" stroke="#444" stroke-width="2.4" stroke-linecap="round"><circle cx="10" cy="10" r="7"/><path d="M15 15l6 6"/></svg></div>
    <div style="background:#a2a7aa"><svg width="18" height="18" viewBox="0 0 24 24" fill="none" stroke="#444" stroke-width="1.4"><circle cx="12" cy="12" r="9"/><path d="M8 10h8M8 13h8M8 16h5"/></svg></div>
    <div style="background:var(--slate)"><svg width="20" height="20" viewBox="0 0 24 24" fill="none" stroke="#fff" stroke-width="1.6"><circle cx="12" cy="12" r="10"/><circle cx="12" cy="10" r="3.5"/><path d="M5.5 19a8 8 0 0 1 13 0"/></svg></div>
  </div>
  <div class="abs label" style="left:203px;top:113px;color:var(--slate)">Benefit &amp; Solution</div>
  <p class="abs tiny" style="left:203px;top:122px;width:150px;font-size:4px">Dolor sit amet, consectetuer adipiscing elit, sed diam nonummy nibh euismod tincidunt ut laoreet dolore magna aliquam erat volutpat. Ut wisi enim ad minim veniam, quis nostrud</p>
  <p class="abs tiny" style="left:213px;top:145px;width:140px;color:var(--ink);line-height:1.85;font-size:3.4px">a) Dolor sit amet, consectetuer adipiscing elit,<br>b) Sed diam nonummy nibh euismod tincidunt ut laoreet<br>c) Bolore magna aliquam erat volutpat.<br>d) Ut wisi enim ad minim veniam, quis nostrud exerci<br>e) Tation ullamcorper suscipit lobortis</p>
  <div class="sr-band">
    <p>▪ Consectetuer adipiscing elit, sed diam nonummy nibh euismod tincidunt ut laoreet dolore magna aliquam erat volutpat. Ut wisi enim nisl.</p>
    <p>▪ Lorem ipsum dolor sit amet, consectetuer adipiscing elit, sed diam nonummy nibh euismod tincidunt ut laoreet dolore magna aliquam erat volutpat. Ut wisi enim ad minim veniam,</p>
    <p>▪ Sed diam nonummy nibh euismod tincidunt ut laoreet dolore magna aliquam erat wisi enim nisl.</p>
  </div>
  <div class="circle-ic" style="left:45px"><svg width="16" height="16" viewBox="0 0 16 16" fill="none" stroke="var(--slate)" stroke-width="1"><circle cx="8" cy="8" r="6.5"/><path d="M8 5v6M5 8h6"/></svg></div>
  <div class="circle-ic" style="left:169px"><svg width="16" height="16" viewBox="0 0 16 16" fill="none" stroke="var(--slate)" stroke-width="1"><circle cx="8" cy="8" r="6.5"/><rect x="5" y="5" width="6" height="6"/><path d="M6.5 10V8.5M8 10V7M9.5 10V6"/></svg></div>
  <div class="circle-ic" style="left:293px"><svg width="16" height="16" viewBox="0 0 16 16" fill="none" stroke="var(--slate)" stroke-width="1"><circle cx="8" cy="9" r="5.5"/><circle cx="6" cy="8" r=".5" fill="var(--slate)"/><circle cx="10" cy="8" r=".5" fill="var(--slate)"/><path d="M5.5 10.5a3 3 0 0 0 5 0M8 .8v1.4M4.5 1.8l.7 1.2M11.5 1.8l-.7 1.2"/></svg></div>
  <div class="foot-strip"></div>
</section>

<!-- Knowledge articles -->
<section class="slide knowledge">
  <div class="kn-head" role="img" aria-label="Hands typing on a laptop under a slate blue tint">
    <h2>Knowledge Articles</h2>
    <div class="sub">Find helpful information</div>
    <p class="tiny">Lorem ipsum dolor sit amet, consectetuer adipiscing elit, sed diam nonummy nibh euismod tincidunt ut laoreet dolore magna aliquam erat volutpat. Ut wisi enim ad minim veniam,</p>
    <div class="brand">velora</div>
  </div>
  <div class="heading-h abs" style="left:15px;top:72px">
    <svg width="12" height="12" viewBox="0 0 12 12"><circle cx="6" cy="6" r="6" fill="var(--slate)"/><path d="M6 3l2.6 5H3.4z" fill="#fff"/></svg>Problem
  </div>
  <ul class="abs bullets tiny" style="left:14px;top:89px;width:170px;color:var(--ink);font-size:3.9px">
    <li>Lorem ipsum dolor sit amet, consectetuer adipiscing elit, sed diam nonummy nibh euismod tincidunt ut laoreet dolore magna aliquam erat volutpat.</li>
    <li>Lorem ipsum dolor sit amet, consectetuer adipiscing elit, sed diam nonummy nibh euismod tincidunt ut laoreet dolore magna aliquam erat volutpat.</li>
  </ul>
  <div class="abs tiny" style="left:23px;top:124px;width:150px;border-left:.5px solid var(--slate-light);padding-left:4px;color:var(--ink);font-size:4px;line-height:1.55">
    <b style="color:var(--slate)">Heading: 1</b><br>1. Dolor sit amet, consectetuer adipiscing elit,<br>2. Sed diam nonummy nibh euismod tincidunt ut laoreet<br>3. Bolore magna aliquam erat volutpat.<br>4. Ut wisi enim ad minim veniam, quis nostrud exerci<br>5. Tation ullamcorper suscipit lobortis<br><br>
    <b style="color:var(--slate)">Heading: 2</b><br>1. Dolor sit amet, consectetuer adipiscing elit,<br>2. Sed diam nonummy nibh euismod tincidunt ut laoreet<br>3. Bolore magna aliquam erat volutpat.<br>4. Ut wisi enim ad minim veniam, quis nostrud exerci<br>5. Tation ullamcorper suscipit lobortis
  </div>
  <div class="photo" role="img" aria-label="Close view of hands on a laptop keyboard" style="left:0;top:220px;width:209px;height:42px;background:linear-gradient(90deg,#56636b,#8b9aa3);clip-path:polygon(0 0,88% 0,100% 100%,0 100%)"></div>
  <div class="sol-box">
    <div class="heading-h"><svg width="12" height="12" viewBox="0 0 12 12"><circle cx="6" cy="6" r="6" fill="var(--slate)"/><circle cx="6" cy="6" r="2" fill="none" stroke="#fff" stroke-width="1"/><path d="M6 2v1.5M6 8.5V10M2 6h1.5M8.5 6H10" stroke="#fff" stroke-width="1"/></svg>Solution</div>
    <ul class="bullets tiny" style="margin-top:6px;color:var(--ink);font-size:3.8px">
      <li>Consectetuer adipiscing elit, sed diam nonummy nibh euismod tincidunt ut laoreet dolore magna aliquam erat volutpat. Ut wisi enim nisl.</li>
      <li>Lorem ipsum dolor sit amet, consectetuer adipiscing elit, sed diam nonummy nibh euismod tincidunt ut laoreet dolore magna aliquam erat volutpat. Ut wisi enim ad minim veniam,</li>
      <li>Sed diam nonummy nibh euismod tincidunt ut laoreet dolore magna aliquam erat wisi enim nisl.</li>
      <li>Consectetuer adipiscing elit, sed diam nonummy nibh euismod tincidunt ut laoreet dolore magna aliquam erat volutpat. Ut wisi enim nisl.</li>
    </ul>
    <p class="tiny" style="padding-left:6px;color:var(--ink);line-height:1.8;font-size:3.5px">a) Dolor sit amet, consectetuer adipiscing elit,<br>b) Sed diam nonummy nibh euismod tincidunt ut laoreet<br>c) Bolore magna aliquam erat volutpat.<br>d) Ut wisi enim ad minim veniam, quis nostrud exerci<br>e) Tation ullamcorper suscipit lobortis</p>
  </div>
  <div class="foot-strip"></div>
</section>

<!-- FAQ -->
<section class="slide faq">
  <div class="photo" role="img" aria-label="Faded mountain landscape behind the questions" style="left:0;top:48px;width:370px;height:214px;background:linear-gradient(180deg,#fafafa 0%,#eef1f2 50%,#b9c5cc 100%)"></div>
  <div class="faq-head" role="img" aria-label="Person typing on a laptop in greyscale">
    <h2>FAQ'S</h2>
    <div class="sub">Read important information to releases of Skyline9</div>
    <div class="brand">velora</div>
  </div>
  <div class="qa" style="top:64px"><div class="q"><b>Q</b>How to purchase a membership for Velora?</div><div class="a"><b>A</b><span>Lorem ipsum dolor sit amet, consectetuer adipiscing elit, sed diam nonummy nibh euismod tincidunt ut laoreet dolore magna aliquam erat volutpat. Ut wisi enim ad minim veniam,</span></div></div>
  <div class="qa" style="top:93px"><div class="q"><b>Q</b>How to purchase a membership for Velora?</div><div class="a"><b>A</b><span>Lorem ipsum dolor sit amet, consectetuer adipiscing elit, sed diam nonummy nibh euismod tincidunt ut laoreet dolore magna aliquam erat volutpat. Ut wisi enim ad minim veniam,</span></div></div>
  <div class="qa" style="top:123px"><div class="q"><b>Q</b>How to purchase a membership for Velora?</div><div class="a"><b>A</b><span>Lorem ipsum dolor sit amet, consectetuer adipiscing elit, sed diam nonummy nibh euismod tincidunt ut laoreet dolore magna aliquam erat volutpat. Ut wisi enim ad minim veniam,</span></div></div>
  <div class="qa" style="top:152px;border:0"><div class="q"><b>Q</b>How to purchase a membership for Velora?</div><div class="a"><b>A</b><span>Lorem ipsum dolor sit amet, consectetuer adipiscing elit, sed diam nonummy nibh euismod tincidunt ut laoreet dolore magna aliquam erat volutpat. Ut wisi enim ad minim veniam,</span></div></div>
  <div class="pill hot" style="top:67px"><div class="dot"></div><p>Sed diam nonummy nibh euismod tincidunt ut laoreet dolore magna aliquam erat wisi enim nisl.</p></div>
  <div class="pill" style="top:92px"><div class="dot"></div><p>Sed diam nonummy nibh euismod tincidunt ut laoreet dolore magna aliquam erat wisi enim nisl.</p></div>
  <div class="pill hot" style="top:117px"><div class="dot"></div><p>Sed diam nonummy nibh euismod tincidunt ut laoreet dolore magna aliquam erat wisi enim nisl.</p></div>
  <div class="pill" style="top:142px"><div class="dot"></div><p>Sed diam nonummy nibh euismod tincidunt ut laoreet dolore magna aliquam erat wisi enim nisl.</p></div>
  <div class="faq-panel"></div>
  <div class="person" style="left:70px"><div class="av"></div><p class="tiny">Dolor sit amet, consectetuer adipiscing elit, sed diam nonummy nibh euismod tincidunt ut laoreet dolore magna aliquam erat volutpat.</p><p class="who">@Sam Ortell</p></div>
  <div class="person" style="left:129px"><div class="av"></div><p class="tiny">Lorem ipsum dolor sit amet, consectetuer adipiscing elit, sed diam nonummy nibh euismod tincidunt ut laoreet dolore magna volutpat.</p><p class="who">@ Ida Venn</p></div>
  <div class="person" style="left:189px"><div class="av"></div><p class="tiny">Dolor sit amet, consectetuer adipiscing elit, sed diam nonummy nibh euismod tincidunt ut laoreet dolore magna aliquam erat volutpat.</p><p class="who">@Noa Brill</p></div>
  <div class="person" style="left:247px"><div class="av"></div><p class="tiny">Lorem ipsum dolor sit amet, consectetuer adipiscing elit, sed diam nonummy nibh euismod tincidunt ut laoreet dolore magna volutpat.</p><p class="who">@ Leo Marsh</p></div>
</section>

</body>
</html>
```